Flyer-Design für Autolackiererei
Hallo es muss nur noch die Richtige Telefonnumer rein , die bekomm ich esrt von Fernova zu geschickt
Zielgruppe
Karosserie & Autolackiererei
Autohäuser , Privatkunden , Bussunterhemen , LKW Unterhemen , Versicherungen
Aufgabenstellung
Neueröffung Von Autolackiererei ab 01.03.2019 bitte ganz wichtig muss auf flayer drauf.
Unfallinstansetztung , Fahrzeuglackierung Jeglicher Art , Oldtimer Restauration , Fahrzeugaufbereitung , Achsvermessung ,Felgen Lackieren ,Hagelschaden ,
inspektionen alle Fahrzeug Fabrikaten, Mpk, Reifenservice
Hol und Bring service ,scheibenaustausch abwicklung mit versicherung ,
Smart Repair

```html
<!DOCTYPE html>
<html lang="de">
<head>
<meta charset="utf-8">
<title>Flyer Autolackiererei Brenner – Neueröffnung</title>
<link rel="stylesheet" href="https://fonts.googleapis.com/css2?family=Montserrat:wght@400;500;700;800;900&display=swap">
<style>
  :root {
    --stage: #d0d0d0;
    --paper: #ffffff;
    --ink: #0a0a0a;
    --slate: #727071;
    --tag-grey: #9d9d9d;
    --brand-blue: #1d9bd8;
    --logo-grey: #5f5e60;
    --note-grey: #3a3a3a;
    --photo-light: #f3f3f3;
    --photo-mid: #e2e2e2;
  }
  * { margin: 0; padding: 0; box-sizing: border-box; }
  html, body { width: 1000px; height: 1200px; overflow: hidden; background: var(--stage); }
  body { position: relative; font-family: "Montserrat", Arial, sans-serif; color: var(--ink); }

  .flyer-side { position: absolute; left: 107px; width: 786px; height: 393px; background: var(--paper); overflow: hidden; }
  .flyer-front { top: 170px; }
  .flyer-back { top: 637px; }

  /* front */
  .photo-area {
    position: absolute; left: 196px; top: 70px; width: 590px; height: 311px;
    background: radial-gradient(ellipse at 55% 50%, var(--photo-mid) 0%, var(--photo-light) 55%, var(--paper) 100%);
  }
  .opening-band {
    position: absolute; left: 0; top: 40px; width: 350px; height: 57px;
    background: var(--ink); color: var(--paper);
    font-weight: 900; font-size: 35px; letter-spacing: 1px;
    padding-left: 31px; line-height: 57px;
  }
  .opening-date {
    position: absolute; left: 152px; top: 84px; width: 257px; height: 53px;
    background: var(--tag-grey); transform: rotate(-3deg);
    font-weight: 800; font-size: 29px; line-height: 53px; padding-left: 20px; color: var(--ink);
  }
  .brand-mark { position: absolute; display: flex; align-items: center; justify-content: center; }
  .brand-mark svg { position: absolute; inset: 0; }
  .brand-name {
    position: relative; font-weight: 700; color: var(--logo-grey);
    text-align: center; line-height: 1.15;
  }
  .front-mark { left: 98px; top: 162px; width: 188px; height: 188px; }
  .front-mark .brand-name { font-size: 19px; }
  .front-claim {
    position: absolute; right: 40px; top: 310px; text-align: right;
    font-weight: 800; font-size: 20px; line-height: 26px; letter-spacing: 0.5px;
  }
  .front-claim .accent { color: var(--brand-blue); }

  /* back */
  .services-panel {
    position: absolute; left: 0; top: 0; width: 525px; height: 393px;
    background: var(--slate); padding: 36px 0 0 28px;
  }
  .services-main { list-style: none; font-weight: 800; font-size: 20px; color: var(--paper); letter-spacing: 0.4px; }
  .services-main li { height: 27px; line-height: 27px; white-space: nowrap; }
  .services-more { list-style: none; margin-top: 20px; font-weight: 800; font-size: 14.5px; color: var(--ink); letter-spacing: 0.6px; }
  .services-more li { height: 24px; line-height: 24px; white-space: nowrap; }
  .services-main li::before, .services-more li::before { content: "· "; }
  .services-more .note {
    display: block; font-size: 10.5px; line-height: 12px; color: var(--note-grey);
    margin: -3px 0 0 10px; letter-spacing: 0.4px;
  }
  .services-more li.with-note { height: 39px; }

  .contact-panel { position: absolute; left: 525px; top: 0; width: 261px; height: 393px; text-align: center; }
  .back-mark { left: 55px; top: 47px; width: 150px; height: 150px; }
  .back-mark .brand-name { font-size: 15px; }
  .contact-panel .claim {
    position: absolute; left: 0; right: 0; top: 221px;
    font-weight: 800; font-size: 13px; letter-spacing: 5.5px; color: var(--brand-blue); padding-left: 6px;
  }
  .contact-lines { position: absolute; left: 0; right: 0; top: 264px; font-style: normal; font-size: 12.5px; line-height: 23.8px; color: var(--ink); }
</style>
</head>
<body>
  <section class="flyer-side flyer-front">
    <div class="photo-area" role="img" aria-label="Foto: Miniaturfiguren von Lackierern an einem weißen Modellauto"></div>
    <div class="opening-band">NEUERÖFFUNG</div>
    <div class="opening-date">ab 01.03.2019</div>
    <div class="brand-mark front-mark">
      <svg viewBox="0 0 188 188"><circle cx="94" cy="94" r="88" fill="none" stroke="var(--brand-blue)" stroke-width="6"/></svg>
      <div class="brand-name">Lackiererei<br>Brenner</div>
    </div>
    <div class="front-claim">AUTOLACKIEREREI<br><span class="accent">MEISTERBETRIEB</span></div>
  </section>

  <section class="flyer-side flyer-back">
    <div class="services-panel">
      <ul class="services-main">
        <li>FAHRZEUGLACKIERUNG JEGLICHER ART</li>
        <li>FELGEN LACKIEREN</li>
        <li>OLDTIMER RESTAURATION</li>
      </ul>
      <ul class="services-more">
        <li>INSPEKTIONEN ALLER FAHRZEUG-FABRIKATEN | MPK</li>
        <li>UNFALLINSTANSETZTUNG</li>
        <li>ACHSVERMESSUNG</li>
        <li class="with-note">SCHEIBENAUSTAUSCH<span class="note">(ABWICKLUNG MIT DER VERSICHERUNG)</span></li>
        <li>REIFENSERVICE</li>
        <li>FAHRZEUGAUFBEREITUNG</li>
        <li>HAGELSCHADEN</li>
        <li>SMART REPAIR</li>
        <li>HOL- &amp; BRING-SERVICE</li>
      </ul>
    </div>
    <div class="contact-panel">
      <div class="brand-mark back-mark">
        <svg viewBox="0 0 150 150"><circle cx="75" cy="75" r="70" fill="none" stroke="var(--brand-blue)" stroke-width="5"/></svg>
        <div class="brand-name">Lackiererei<br>Brenner</div>
      </div>
      <div class="claim">MEISTERBETRIEB</div>
      <address class="contact-lines">
        Lackweg 7,<br>
        54321 Hausen<br>
        +49(0)321 98 76 540<br>
        info@lackiererei-brenner.de
      </address>
    </div>
  </section>
</body>
</html>
```